Blue Heron Business Card

This is a business card for a printing company but I actually don't have a logo. Just need to typeset the words "Blue Heron Printing" as the logo. Then add my name "Marla Vossen" + phone number + address

Target Market(s)

ceos and professionals

Industry/Entity Type

printing and manufacturing

Contact Information for Business Card

Blue Heron Printing/ 4817 dunmore ave. S. El Monte, CA 90418/ 626-447-3092/ Marla Vossen

Font styles to use
Serif
Other font styles liked:
• a modern font would be nice

Colors
0054AA
0677BA
7BADD7
CADEEF
E8F1F8
0094D4
00A9DD
6FCCEA
C7EBF8
E9F6FB

Requirements
Must have
• company name, number, address
Nice to have
• nice bold feel
Should not have
• nothing in particular

```html
<!DOCTYPE html>
<html lang="en">
<head>
<meta charset="utf-8">
<title>Blue Heron Business Card</title>
<link rel="stylesheet" href="https://fonts.googleapis.com/css2?family=Roboto:wght@400;500&family=Roboto+Condensed:wght@500;700&display=swap">
<style>
  :root {
    --backdrop: #2a2a2a;
    --card-blue: #0a6db3;
    --card-blue-deep: #0862a3;
    --brand-blue: #0c65a8;
    --mark-light: #7badd7;
    --paper: #f2f2f2;
    --paper-shade: #e6e6e6;
    --ink: #333a40;
    --rule: #3a3f44;
    --white: #ffffff;
    --band-text: #e9f1f8;
  }
  * { margin: 0; padding: 0; box-sizing: border-box; }
  html, body { width: 1200px; height: 1138px; overflow: hidden; }
  body {
    background: var(--backdrop);
    position: relative;
    font-family: "Roboto", Arial, sans-serif;
  }
  .card {
    position: absolute;
    border-radius: 16px;
    overflow: hidden;
  }
  .card--front {
    left: 274px; top: 185px; width: 623px; height: 377px;
    background: linear-gradient(180deg, var(--card-blue) 0%, var(--card-blue-deep) 100%);
  }
  .card--back {
    left: 276px; top: 607px; width: 618px; height: 375px;
    background: linear-gradient(180deg, var(--paper) 0%, var(--paper-shade) 85%);
  }
  .brand {
    position: absolute;
    text-align: center;
    font-family: "Roboto", Arial, sans-serif;
    font-weight: 500;
  }
  .brand__square {
    display: block;
    width: 62px; height: 62px;
    margin: 0 auto 30px;
  }
  .brand__name {
    display: block;
    font-size: 39px;
    line-height: 1;
    letter-spacing: 0.5px;
  }
  .brand__tag {
    display: block;
    font-size: 19px;
    letter-spacing: 15px;
    margin-top: 9px;
    padding-left: 15px;
  }
  .card--front .brand {
    left: 0; right: 0; top: 90px;
    color: var(--white);
  }
  .card--front .brand__square { background: var(--mark-light); }
  .card--back .brand {
    left: 54px; width: 260px; top: 98px;
    color: var(--brand-blue);
  }
  .card--back .brand__square { background: var(--brand-blue); }
  .card--back .brand__name { font-size: 34px; }
  .card--back .brand__tag { font-size: 17px; letter-spacing: 13px; }
  .contact {
    position: absolute;
    left: 362px; top: 88px;
    color: var(--ink);
  }
  .contact__name {
    font-family: "Roboto Condensed", Arial, sans-serif;
    font-weight: 700;
    font-size: 26px;
    color: var(--brand-blue);
    line-height: 1.1;
  }
  .contact__role {
    font-size: 16px;
    margin-top: 3px;
  }
  .contact__list {
    list-style: none;
    margin-top: 20px;
    font-size: 16.5px;
    line-height: 25px;
  }
  .contact__item {
    position: relative;
    padding-left: 30px;
  }
  .contact__icon {
    position: absolute;
    left: 0; top: 4px;
    width: 17px; height: 17px;
  }
  .card__rule {
    position: absolute;
    left: 0; right: 0; top: 326px;
    height: 3px;
    background: var(--rule);
  }
  .card__band {
    position: absolute;
    left: 0; right: 0; bottom: 0;
    height: 40px;
    background: var(--brand-blue);
    color: var(--band-text);
    font-family: "Roboto Condensed", Arial, sans-serif;
    font-weight: 700;
    font-size: 19px;
    text-align: center;
    line-height: 40px;
  }
</style>
</head>
<body>
  <section class="card card--front" aria-label="Card front">
    <div class="brand">
      <span class="brand__square"></span>
      <span class="brand__name">BLUE HERON</span>
      <span class="brand__tag">PRINTING</span>
    </div>
  </section>

  <section class="card card--back" aria-label="Card back">
    <div class="brand">
      <span class="brand__square"></span>
      <span class="brand__name">BLUE HERON</span>
      <span class="brand__tag">PRINTING</span>
    </div>
    <div class="contact">
      <p class="contact__name">Marla Vossen</p>
      <p class="contact__role">Managing Director</p>
      <ul class="contact__list">
        <li class="contact__item">
          <svg class="contact__icon" viewBox="0 0 20 20" aria-hidden="true">
            <circle cx="10" cy="10" r="8.5" fill="none" stroke="#0c65a8" stroke-width="1.8"/>
            <path d="M7 5.5c-.8.4-1.4 1.2-1 2.6.7 2.5 3.4 5.2 5.9 5.9 1.4.4 2.2-.2 2.6-1l-1.8-1.4-1.1.8c-1.2-.5-2.5-1.8-3-3l.8-1.1z" fill="#0c65a8"/>
          </svg>
          626-447-3092
        </li>
        <li class="contact__item">
          <svg class="contact__icon" viewBox="0 0 20 20" aria-hidden="true">
            <path d="M10 1a6.5 6.5 0 0 0-6.5 6.5C3.5 12 10 19 10 19s6.5-7 6.5-11.5A6.5 6.5 0 0 0 10 1z" fill="#0c65a8"/>
            <circle cx="10" cy="7.5" r="2.4" fill="#f2f2f2"/>
          </svg>
          4817 Dunmore AVE. S.<br>El Monte, CA 90418
        </li>
      </ul>
    </div>
    <div class="card__rule"></div>
    <div class="card__band">THE BLUE HERON PRINTING</div>
  </section>
</body>
</html>
```